CASH PAYMENT DISCOUNT NOTICE POSTED IN CASH REGISTER AREA

LOOKING TO MAKE A FLYER OR A POSTED NOTICE FOR CUSTOMERS PAYING FOR OVER-THE-COUNTER MERCHANDISE AND WHO PAY BY CASH METHOD TO GET A 4% CASH DISCOUNT.
PRESCRIPTIONS ARE EXCLUDED FROM THIS CASH DISCOUNT.

Target Market(s)

RETAIL CUSTOMERS

Industry/Entity Type

RETAIL PHARMACY

Colors
0054AA
0677BA
7BADD7
CADEEF
E8F1F8
EB3D1F
EC4F4E
F09395
F8D3D4
FCEDEE

Requirements
Must have
• LOGO COLORS
Nice to have
• EYE CATCHING

```html
<!DOCTYPE html>
<html lang="en">
<head>
<meta charset="utf-8">
<title>4% Cash Discount Notice – Design Options</title>
<link rel="stylesheet" href="https://fonts.googleapis.com/css2?family=Open+Sans:wght@800&family=Noticia+Text&display=swap">
<style>
  :root {
    --board-bg: #fcfae8;
    --card-bg: #ffffff;
    --card-bg-soft: #fbfaf8;
    --brand-red: #b01c1c;
    --brand-red-deep: #8a1a1a;
    --brand-blue: #2a4d9b;
    --brand-blue-deep: #243a75;
    --headline-font: "Open Sans", Arial, sans-serif;
    --body-font: "Noticia Text", Georgia, serif;
  }
  * { margin: 0; padding: 0; box-sizing: border-box; }
  html, body { width: 1200px; height: 1200px; overflow: hidden; }
  body { background: var(--board-bg); position: relative; }
  .option-label {
    position: absolute;
    top: 212px;
    width: 513.6px;
    text-align: center;
    font-family: var(--headline-font);
    font-weight: 800;
    font-size: 25px;
    letter-spacing: 0.5px;
    color: var(--brand-red);
  }
  .notice-card {
    position: absolute;
    top: 264px;
    width: 513.6px;
    height: 726.4px;
    box-shadow: 10px 10px 18px rgba(60, 50, 30, 0.35);
  }
  .notice-card svg { display: block; width: 100%; height: 100%; }
  .option-one { left: 65.6px; }
  .option-two { left: 625px; }
  .headline { font-family: var(--headline-font); font-weight: 800; }
  .discount-figure { fill: var(--brand-red); }
  .cash-line { fill: var(--brand-blue); font-size: 60px; }
  .exclusion-note { font-family: var(--body-font); fill: var(--brand-blue); font-size: 30px; }
</style>
</head>
<body>

<div class="option-label" style="left:65.6px">DESIGN OPTION 1</div>
<div class="option-label" style="left:625px">DESIGN OPTION 2</div>

<div class="notice-card option-one">
  <svg viewBox="0 0 642 908" xmlns="http://www.w3.org/2000/svg">
    <defs>
      <linearGradient id="blue-band-1" x1="0" y1="0" x2="1" y2="0">
        <stop offset="0" stop-color="#2a4fa0"/>
        <stop offset="1" stop-color="#24356c"/>
      </linearGradient>
      <linearGradient id="red-band-1" x1="0" y1="0" x2="1" y2="1">
        <stop offset="0" stop-color="#b01c1c"/>
        <stop offset="1" stop-color="#881a1a"/>
      </linearGradient>
    </defs>
    <rect class="card-surface" width="642" height="908" fill="var(--card-bg)"/>
    <text class="headline discount-figure" x="128" y="373" font-size="347" textLength="195" lengthAdjust="spacingAndGlyphs">4</text>
    <text class="headline discount-figure" x="316" y="282" font-size="190" textLength="165" lengthAdjust="spacingAndGlyphs">%</text>
    <text class="headline discount-figure" x="350" y="358" font-size="77" textLength="131" lengthAdjust="spacingAndGlyphs">OFF</text>
    <text class="headline cash-line" x="321" y="462" text-anchor="middle" textLength="427" lengthAdjust="spacingAndGlyphs">WHEN YOU PAY</text>
    <text class="headline cash-line" x="321" y="522" text-anchor="middle" textLength="233" lengthAdjust="spacingAndGlyphs">BY CASH</text>
    <text class="exclusion-note" x="321" y="607" text-anchor="middle" textLength="422" lengthAdjust="spacingAndGlyphs">Cash discount not applicable</text>
    <text class="exclusion-note" x="321" y="645" text-anchor="middle" textLength="395" lengthAdjust="spacingAndGlyphs">for prescription purchases.</text>
    <path class="wave-blue" fill="url(#blue-band-1)" d="M0,670 C60,740 150,762 260,762 C360,762 420,730 520,712 C580,702 620,708 642,712 L642,908 L0,908 Z"/>
    <path class="wave-red" fill="url(#red-band-1)" d="M0,762 C90,800 220,815 330,800 C420,785 460,740 560,724 C600,718 630,718 642,718 L642,908 L0,908 Z"/>
  </svg>
</div>

<div class="notice-card option-two">
  <svg viewBox="0 0 642 908" xmlns="http://www.w3.org/2000/svg">
    <defs>
      <linearGradient id="blue-band-2" x1="0" y1="0" x2="1" y2="0">
        <stop offset="0" stop-color="#2a4fa0"/>
        <stop offset="1" stop-color="#24356c"/>
      </linearGradient>
      <linearGradient id="red-band-2" x1="0" y1="0" x2="1" y2="1">
        <stop offset="0" stop-color="#b01c1c"/>
        <stop offset="1" stop-color="#881a1a"/>
      </linearGradient>
      <radialGradient id="pill-haze" cx="0.5" cy="0.6" r="0.6">
        <stop offset="0" stop-color="#f3dada"/>
        <stop offset="0.5" stop-color="#f1e8ea"/>
        <stop offset="1" stop-color="#fbfaf8" stop-opacity="0"/>
      </radialGradient>
    </defs>
    <rect class="card-surface" width="642" height="908" fill="var(--card-bg-soft)"/>
    <rect class="photo-backdrop" x="20" y="500" width="602" height="280" fill="url(#pill-haze)" role="img" aria-label="Soft-focus photo of scattered medicine tablets and capsules"/>
    <text class="headline discount-figure" x="128" y="373" font-size="347" textLength="195" lengthAdjust="spacingAndGlyphs">4</text>
    <text class="headline discount-figure" x="316" y="282" font-size="190" textLength="165" lengthAdjust="spacingAndGlyphs">%</text>
    <text class="headline discount-figure" x="350" y="358" font-size="77" textLength="131" lengthAdjust="spacingAndGlyphs">OFF</text>
    <text class="headline cash-line" x="321" y="462" text-anchor="middle" textLength="427" lengthAdjust="spacingAndGlyphs">WHEN YOU PAY</text>
    <text class="headline cash-line" x="321" y="522" text-anchor="middle" textLength="233" lengthAdjust="spacingAndGlyphs">BY CASH</text>
    <text class="exclusion-note" x="321" y="594" text-anchor="middle" textLength="422" lengthAdjust="spacingAndGlyphs">Cash discount not applicable</text>
    <text class="exclusion-note" x="321" y="632" text-anchor="middle" textLength="395" lengthAdjust="spacingAndGlyphs">for prescription purchases.</text>
    <path class="wave-blue" fill="url(#blue-band-2)" d="M0,670 C60,740 150,762 260,762 C360,762 420,730 520,712 C580,702 620,708 642,712 L642,908 L0,908 Z"/>
    <path class="wave-red" fill="url(#red-band-2)" d="M0,762 C90,800 220,815 330,800 C420,785 460,740 560,724 C600,718 630,718 642,718 L642,908 L0,908 Z"/>
  </svg>
</div>

</body>
</html>
```